Design a roll up Banner

Design a roll up banner, dimension 85x200 cm, you can see some designs i used to use before, you can use this as some estimate template. Don't use Morvane trucks logo.

```html
<!DOCTYPE html>
<html lang="en">
<head>
<meta charset="utf-8">
<title>Hydrovant roll-up banner</title>
<link rel="stylesheet" href="https://fonts.googleapis.com/css2?family=Oswald:wght@600;700&family=Mulish:wght@400;600;700&display=swap">
<style>
  :root {
    --navy: #1f3a6e;
    --navy-deep: #162b55;
    --blue: #2a4f94;
    --white: #ffffff;
    --text-dark: #2b2e33;
    --text-navy: #1c2f5c;
    --band-text: #e9edf5;
  }
  html, body {
    margin: 0;
    padding: 0;
    width: 717px;
    height: 1200px;
    overflow: hidden;
    background: var(--white);
  }
  .banner {
    position: relative;
    width: 717px;
    height: 1200px;
    overflow: hidden;
    background: var(--white);
    font-family: "Mulish", sans-serif;
    color: var(--text-dark);
  }
  .top-band {
    position: absolute;
    left: 0; top: 0;
    width: 717px; height: 116px;
    background: radial-gradient(ellipse at 50% 40%, #3c3f45 0%, #1e2024 70%, #141518 100%);
  }
  .brand-plate {
    position: absolute;
    left: 181px; top: 20px;
    width: 344px; height: 143px;
    background: linear-gradient(180deg, #ffffff 0%, #eef0f3 60%, #d6d9de 100%);
    border: 5px solid #b9bdc4;
    box-sizing: border-box;
    box-shadow: 0 6px 12px rgba(0,0,0,0.35);
    display: flex;
    flex-direction: column;
    align-items: center;
    justify-content: center;
    gap: 10px;
  }
  .brand-mark {
    width: 52px; height: 52px;
    border-radius: 50%;
    background: var(--navy);
  }
  .brand-name {
    font-weight: 700;
    font-size: 32px;
    letter-spacing: 1px;
    color: var(--text-navy);
  }
  .headline {
    position: absolute;
    left: 0; top: 180px;
    width: 717px;
    margin: 0;
    text-align: center;
    font-family: "Oswald", sans-serif;
    font-weight: 700;
    font-size: 64px;
    line-height: 64px;
    color: var(--navy);
  }
  .services {
    position: absolute;
    left: 45px; top: 247px;
    margin: 0; padding: 0;
    list-style: none;
  }
  .services li {
    display: flex;
    align-items: center;
    gap: 14px;
    height: 39px;
    font-size: 33px;
    font-weight: 400;
    color: var(--text-dark);
  }
  .services svg { width: 22px; height: 22px; flex: none; }
  .product-field {
    position: absolute;
    left: 0; top: 0;
    width: 717px; height: 1200px;
  }
  .product-photo {
    position: absolute;
    width: 176px; height: 176px;
    border-radius: 50%;
    border: 7px solid #e6e8ec;
    box-sizing: border-box;
    background: radial-gradient(circle at 50% 45%, #ffffff 0%, #e9ebee 55%, #b7bbc2 100%);
    box-shadow: 0 4px 10px rgba(0,0,0,0.5);
  }
  .highlights {
    position: absolute;
    left: 39px; top: 912px;
    width: 645px; height: 116px;
    background: linear-gradient(180deg, #ffffff 0%, #eceef1 55%, #c7cbd1 100%);
    box-shadow: 0 5px 10px rgba(0,0,0,0.3);
    display: flex;
    flex-direction: column;
    align-items: center;
    justify-content: center;
    gap: 8px;
    font-size: 23px;
    color: var(--text-navy);
  }
  .highlights p { margin: 0; }
  .contact-band {
    position: absolute;
    left: 0; top: 1056px;
    width: 717px; height: 91px;
    background: var(--navy-deep);
    color: var(--band-text);
    font-size: 17px;
  }
  .contact-col {
    position: absolute;
    top: 8px;
    margin: 0; padding: 0;
    list-style: none;
  }
  .contact-col li {
    display: flex;
    align-items: center;
    gap: 9px;
    height: 25px;
  }
  .contact-col.phones { left: 66px; }
  .contact-col.online { left: 271px; }
  .contact-icon { width: 18px; height: 18px; flex: none; }
  .partner-strip {
    position: absolute;
    left: 0; top: 1147px;
    width: 717px; height: 53px;
    display: flex;
    align-items: center;
    justify-content: space-around;
    padding: 0 60px;
    box-sizing: border-box;
  }
  .partner {
    font-weight: 700;
    font-size: 24px;
    color: var(--text-navy);
  }
  .partner-badge {
    width: 34px; height: 42px;
    background: var(--blue);
  }
</style>
</head>
<body>
<main class="banner">
  <div class="top-band" role="img" aria-label="Dark metallic hexagon mesh texture"></div>

  <div class="brand-plate">
    <div class="brand-mark"></div>
    <div class="brand-name">HYDROVANT</div>
  </div>

  <h1 class="headline">YOU CARE YOUR SPARE</h1>

  <ul class="services">
    <li><svg viewBox="0 0 20 20"><rect x="2" y="4" width="14" height="14" fill="none" stroke="#2a4f94" stroke-width="2"/><path d="M5 10 L9 14 L18 3" fill="none" stroke="#2a4f94" stroke-width="2.4"/></svg>Spare parts sale</li>
    <li><svg viewBox="0 0 20 20"><rect x="2" y="4" width="14" height="14" fill="none" stroke="#2a4f94" stroke-width="2"/><path d="M5 10 L9 14 L18 3" fill="none" stroke="#2a4f94" stroke-width="2.4"/></svg>Truck and Trailer Service</li>
    <li><svg viewBox="0 0 20 20"><rect x="2" y="4" width="14" height="14" fill="none" stroke="#2a4f94" stroke-width="2"/><path d="M5 10 L9 14 L18 3" fill="none" stroke="#2a4f94" stroke-width="2.4"/></svg>Morvane Trucks Service</li>
    <li><svg viewBox="0 0 20 20"><rect x="2" y="4" width="14" height="14" fill="none" stroke="#2a4f94" stroke-width="2"/><path d="M5 10 L9 14 L18 3" fill="none" stroke="#2a4f94" stroke-width="2.4"/></svg>Steinwalder and Korvan Service</li>
  </ul>

  <svg class="product-field" viewBox="0 0 717 1200" role="img" aria-label="Dark hexagon mesh background framed by navy curves">
    <defs>
      <radialGradient id="meshTone" cx="50%" cy="55%" r="65%">
        <stop offset="0%" stop-color="#45484e"/>
        <stop offset="70%" stop-color="#25272b"/>
        <stop offset="100%" stop-color="#18191c"/>
      </radialGradient>
    </defs>
    <path d="M0 432 Q360 418 717 400 L717 925 L0 925 Z" fill="#1f3a6e"/>
    <path d="M0 446 Q360 432 717 416 L717 905 Q358 860 0 905 Z" fill="url(#meshTone)"/>
    <path d="M0 925 Q358 882 717 925 L717 940 L0 940 Z" fill="#ffffff"/>
  </svg>

  <div class="product-photo" style="left:44px; top:486px;" role="img" aria-label="Photo of an air brake valve"></div>
  <div class="product-photo" style="left:273px; top:486px;" role="img" aria-label="Photo of a truck brake caliper"></div>
  <div class="product-photo" style="left:499px; top:486px;" role="img" aria-label="Photo of a brake disc"></div>
  <div class="product-photo" style="left:44px; top:671px;" role="img" aria-label="Photo of an air compressor"></div>
  <div class="product-photo" style="left:273px; top:671px;" role="img" aria-label="Photo of a brake chamber"></div>
  <div class="product-photo" style="left:499px; top:671px;" role="img" aria-label="Photo of an EBS control module"></div>

  <section class="highlights">
    <p>Over 6000 articales of spare parts on Stock</p>
    <p>Brake Caliper repair</p>
    <p>Diagnostics EBS,ABS for: Valtrix Norrden and Halvik</p>
  </section>

  <section class="contact-band">
    <ul class="contact-col phones">
      <li><svg class="contact-icon" viewBox="0 0 18 18"><circle cx="9" cy="9" r="8" fill="none" stroke="#e9edf5" stroke-width="1.3"/><rect x="5" y="7" width="8" height="5" rx="1" fill="#e9edf5"/></svg>042-555-101</li>
      <li><svg class="contact-icon" viewBox="0 0 18 18"><circle cx="9" cy="9" r="8" fill="none" stroke="#e9edf5" stroke-width="1.3"/><path d="M6 5 L8 7 L7 8.5 Q8 10.5 9.5 11 L11 10 L13 12 L11.5 13.5 Q7 13 4.5 6.5 Z" fill="#e9edf5"/></svg>098-555-204</li>
      <li><svg class="contact-icon" viewBox="0 0 18 18"><circle cx="9" cy="9" r="8" fill="none" stroke="#e9edf5" stroke-width="1.3"/><rect x="5" y="6" width="8" height="7" rx="1" fill="#e9edf5"/></svg>042-555-317</li>
    </ul>
    <ul class="contact-col online">
      <li><svg class="contact-icon" viewBox="0 0 18 18"><circle cx="9" cy="9" r="8" fill="none" stroke="#e9edf5" stroke-width="1.3"/><circle cx="9" cy="9" r="4" fill="none" stroke="#e9edf5" stroke-width="1.2"/><line x1="5" y1="9" x2="13" y2="9" stroke="#e9edf5" stroke-width="1.2"/></svg>www.hydrovant.hr</li>
      <li><svg class="contact-icon" viewBox="0 0 18 18"><circle cx="9" cy="9" r="8" fill="none" stroke="#e9edf5" stroke-width="1.3"/><rect x="5" y="6" width="8" height="6" fill="none" stroke="#e9edf5" stroke-width="1.2"/><path d="M5 6 L9 9.5 L13 6" fill="none" stroke="#e9edf5" stroke-width="1.2"/></svg>info@hydrovant.hr</li>
      <li><svg class="contact-icon" viewBox="0 0 18 18"><circle cx="9" cy="9" r="8" fill="none" stroke="#e9edf5" stroke-width="1.3"/><path d="M9 14 L6 9 A3 3 0 1 1 12 9 Z" fill="#e9edf5"/></svg>Lipova 14, 42000 Borovec Gornji</li>
    </ul>
  </section>

  <section class="partner-strip">
    <div class="partner-badge" role="img" aria-label="Service partner badge"></div>
    <div class="partner">Korvan</div>
    <div class="partner">Valtrix</div>
  </section>
</main>
</body>
</html>
```